Supplement Rebranding Bottle Design

READ WORD DOCUMENT ATTACHED.
We want to rebrand our current health supplements (see below). We do want it to be modern, vibrant and appealing. Very upscale and elegant as it targets primarily women.
Bottle size: see pictures for bottle size, along with sample bottles that we like; we’re open to any bottle similar to the ones attached.
Current bottles: So ideally, we’d keep the core color on each bottle with a new branding/bottle design. But we're open to your suggestion.

Target Market(s)

mostly women but shouldn't be overly feminine

Requirements
Must have
• see bottle sizes attached

```html
<!DOCTYPE html>
<html lang="en">
<head>
<meta charset="utf-8">
<title>Velunae Supplement Range</title>
<link rel="stylesheet" href="https://fonts.googleapis.com/css2?family=Montserrat:wght@400;500;600&display=swap">
<style>
  :root {
    --bg-centre: #ffffff;
    --bg-edge: #c6c6c6;
    --cap-light: #e6e6e6;
    --cap-dark: #b4b4b4;
    --glass: #f2f2f2;
    --ink: #ffffff;
    --liver: #df4f9c;
    --tummy: #e3250f;
    --hormone: #38d68b;
    --glucose: #2338dd;
  }
  * { margin: 0; padding: 0; box-sizing: border-box; }
  html, body { width: 1200px; height: 637px; overflow: hidden; }
  body {
    position: relative;
    font-family: "Montserrat", sans-serif;
    background: radial-gradient(ellipse 70% 75% at 50% 45%, var(--bg-centre) 0%, #f1f1f1 45%, var(--bg-edge) 100%);
  }
  .bottle { position: absolute; top: 126px; width: 212px; height: 405px; }
  .bottle--liver   { left: 79px;  --tone: var(--liver); }
  .bottle--tummy   { left: 356px; --tone: var(--tummy); }
  .bottle--hormone { left: 633px; --tone: var(--hormone); }
  .bottle--glucose { left: 909px; --tone: var(--glucose); }

  .bottle__cap {
    position: absolute; left: 20px; top: 0; width: 174px; height: 58px;
    border-radius: 4px 4px 2px 2px;
    background: linear-gradient(180deg, var(--cap-light), var(--cap-dark) 45%, #d8d8d8 80%, #c2c2c2);
  }
  .bottle__neck {
    position: absolute; left: 26px; top: 58px; width: 160px; height: 34px;
    border-radius: 6px;
    background: linear-gradient(180deg, #dcdcdc, var(--glass) 50%, #e4e4e4);
  }
  .bottle__body {
    position: absolute; left: 0; top: 86px; width: 212px; height: 319px;
    border-radius: 34px 34px 26px 26px;
    overflow: hidden;
  }
  .bottle__fill {
    position: absolute; inset: 0;
    background: linear-gradient(180deg, var(--glass) 0%, #ececec 18%,
      color-mix(in srgb, var(--tone) 35%, #f2f2f2) 52%,
      color-mix(in srgb, var(--tone) 75%, #ffffff) 80%,
      var(--tone) 100%);
  }
  .label { position: absolute; inset: 0; color: var(--ink); }
  .label__type {
    position: absolute; left: 24px; top: 36px;
    font-size: 11px; font-weight: 500; line-height: 1.15;
    white-space: nowrap;
  }
  .label__claim {
    position: absolute; left: 24px; top: 204px;
    font-size: 12px; font-weight: 600; line-height: 1.02;
    white-space: nowrap;
  }
  .label__count {
    position: absolute; left: 24px; top: 264px;
    font-size: 12px; font-weight: 400; line-height: 1.02;
    white-space: nowrap;
  }
  .label__brand {
    position: absolute; left: 168px; top: 216px;
    width: 190px;
    transform: rotate(-90deg); transform-origin: top left;
    font-size: 15px; font-weight: 600; line-height: 1;
    white-space: nowrap;
  }
</style>
</head>
<body>
  <section class="bottle bottle--liver">
    <div class="bottle__cap"></div>
    <div class="bottle__neck"></div>
    <div class="bottle__body">
      <div class="bottle__fill" role="img" aria-label="Pink capsules seen through frosted bottle"></div>
      <div class="label">
        <p class="label__type">Dietary<br>Supplement</p>
        <p class="label__brand">Velunae Liver</p>
        <p class="label__claim">Rejuvenating<br>Cleanse &amp; Detox<br>Formula*</p>
        <p class="label__count">120 Vegetable<br>Capsules</p>
      </div>
    </div>
  </section>

  <section class="bottle bottle--tummy">
    <div class="bottle__cap"></div>
    <div class="bottle__neck"></div>
    <div class="bottle__body">
      <div class="bottle__fill" role="img" aria-label="Red capsules seen through frosted bottle"></div>
      <div class="label">
        <p class="label__type">Dietary<br>Supplement</p>
        <p class="label__brand">Velunae Tummy</p>
        <p class="label__claim">Oxygenating<br>Colon Cleanse*</p>
        <p class="label__count">90 Vegetable<br>Capsules</p>
      </div>
    </div>
  </section>

  <section class="bottle bottle--hormone">
    <div class="bottle__cap"></div>
    <div class="bottle__neck"></div>
    <div class="bottle__body">
      <div class="bottle__fill" role="img" aria-label="Green capsules seen through frosted bottle"></div>
      <div class="label">
        <p class="label__type">Dietary<br>Supplement</p>
        <p class="label__brand">Velunae Hormone</p>
        <p class="label__claim">Supports Healthy<br>Hormone Levels*</p>
        <p class="label__count">60 Vegetable<br>Capsules</p>
      </div>
    </div>
  </section>

  <section class="bottle bottle--glucose">
    <div class="bottle__cap"></div>
    <div class="bottle__neck"></div>
    <div class="bottle__body">
      <div class="bottle__fill" role="img" aria-label="Blue capsules seen through frosted bottle"></div>
      <div class="label">
        <p class="label__type">Dietary<br>Supplement</p>
        <p class="label__brand">Velunae Blood Sugar</p>
        <p class="label__claim">Supports Healthy<br>Blood Glucose<br>Levels*</p>
        <p class="label__count">60 Vegetable<br>Capsules</p>
      </div>
    </div>
  </section>
</body>
</html>
```